Vantor - Adventurous, Fun, Exciting, Social Fitness Club needs a Webpage with attitude!

Vantor... we're a fun, social, outdoor fitness club that needs not just a homepage designed for our website, but in the process a "personality" for our unique, innovative and cheeky brand.
We pride ourselves on getting our members outdoors trying new, exciting physical activities in an effort to find joy in an active lifestyle, and sharing that experience with other like minded people. We offer:
- Personal Training (1-on-1 Fitness Training)
- Group Fitness Classes (Boxing, Pilates, etc)
- Boot Camps (Military Style - Sandbags, Ropes, Tyres, etc)
- Events (Fun Runs, Triathlons, Ocean Swims, Treks, etc)
- Adventures(Machu Picchu Trek, Rock Climbing, Kayaking, etc)
Our tag line is 'No Judgements. No Limits!' The homepage should be exciting, adventurous and innovative, illustrating the values of our brand: possibility, thirst for life, personal accomplishment & freedom. It should be fun, friendly & inviting.
A few of our key benefits to members are:
- No Boring Workouts
- No Joining Fees or Long Term Contracts
- Results Guaranteed
The links below should give you a rough idea of the sort of "feel" we're after (vibrant, active, adventurous ).
http://www.pupiljourneys.com.au/
http://www.layoutgoblin.com/website-templates/31924.html
http://www.layoutgoblin.com/website-templates/32751.html
http://www.pivel.com/
Target Market(s)
Real, Everyday People - Men & Women (30:70) aged mainly between 21-40, who want a more exciting and enjoyable fitness experience than your typical gym offers.
Industry/Entity Type
Fitness
Requirements
Must have
- Strong, uplifting and motivating images of people enjoying fitness/physical activities outdoors

```html
<!DOCTYPE html>
<html lang="en">
<head>
<meta charset="utf-8">
<title>Vantor – Outdoor Fitness Club</title>
<link href="https://fonts.googleapis.com/css2?family=Arimo:wght@400;700&display=swap" rel="stylesheet">
<style>
:root{
  --gold:#f2b416;
  --gold-deep:#e08a0c;
  --orange:#e8521f;
  --orange-light:#f7a030;
  --red:#e3241b;
  --black:#0c0c0c;
  --nav-dark:#1b1b1b;
  --white:#ffffff;
  --yellow-text:#ffe21a;
  --ink:#111111;
}
*{box-sizing:border-box;margin:0;padding:0}
html,body{width:1117px;height:1200px;overflow:hidden}
body{
  position:relative;
  font-family:"Arimo",Arial,sans-serif;
  color:var(--ink);
  background:
    radial-gradient(ellipse at 30% 20%,rgba(255,230,120,.55),transparent 55%),
    radial-gradient(ellipse at 80% 70%,rgba(255,200,60,.5),transparent 60%),
    linear-gradient(160deg,#f5c02a 0%,#e9a413 45%,#f3bc26 75%,#dc9310 100%);
}
.abs{position:absolute}

/* header */
.site-header{left:26px;top:9px;width:1067px;height:217px;border-radius:12px;overflow:hidden;
  box-shadow:0 2px 6px rgba(0,0,0,.35);
  background:linear-gradient(180deg,#f6c21e 0%,#f49a1c 45%,#e9541f 75%,#e24a1c 100%);}
.brand{left:18px;top:48px;display:flex;align-items:center;gap:12px}
.brand-dot{width:46px;height:46px;border-radius:50%;background:var(--black)}
.brand-name{font-weight:700;font-size:62px;color:var(--black);letter-spacing:1px;line-height:1}
.call{left:694px;top:11px;display:flex;align-items:center;gap:12px;color:var(--white)}
.call-icon{width:64px;height:64px;border-radius:50%;background:radial-gradient(circle at 40% 35%,#ff8a50,#e2361a);border:3px solid #fbd9b4;display:flex;align-items:center;justify-content:center}
.call-text{font-size:31px;text-shadow:0 1px 3px rgba(0,0,0,.4)}
.call-text b{font-weight:700}
.quick-links{left:585px;top:112px;display:flex;gap:22px}
.quick-link{display:flex;align-items:center;gap:10px;color:var(--white);font-weight:700;font-size:15px;text-shadow:0 1px 2px rgba(0,0,0,.4);text-decoration:none}
.quick-link svg{width:50px;height:50px}
.main-nav{left:0;top:171px;width:1067px;height:46px;display:flex;
  background:linear-gradient(180deg,#5a5a5a 0%,#2a2a2a 40%,#0d0d0d 100%)}
.main-nav a{display:flex;align-items:center;padding:0 22px;color:var(--white);font-weight:700;font-size:13px;text-decoration:none;border-right:1px solid #555}
.main-nav a.current{background:linear-gradient(180deg,#fbb23a,#e8521f);width:86px;justify-content:center;padding:0}

/* feature panel */
.feature{left:25px;top:243px;width:1068px;height:346px;border-radius:12px;
  background:linear-gradient(180deg,#fbcf4a,#f3a82a);border:2px solid #fff3c0;box-shadow:0 2px 6px rgba(0,0,0,.3)}
.slider{left:8px;top:8px;width:721px;height:325px;border-radius:12px;overflow:hidden;
  background:linear-gradient(110deg,#8b8f7a 0%,#5c6b3c 30%,#7ea54a 55%,#a9c46e 75%,#6b8a3a 100%)}
.slide-caption{left:0;top:147px;width:480px;height:178px;padding:10px 18px;color:var(--white);
  background:linear-gradient(90deg,rgba(0,0,0,.7) 70%,rgba(0,0,0,0))}
.slide-caption h2{font-size:26px;font-weight:700;margin-bottom:14px}
.slide-caption h3{font-size:15px;font-weight:700;margin:0 0 10px 5px}
.slide-caption p{font-size:12.5px;line-height:16px;margin-left:5px;width:380px}
.slide-caption .more{font-weight:700;margin-top:22px}
.slider-dots{right:34px;bottom:9px;display:flex;gap:5px}
.slider-dots i{width:17px;height:17px;border-radius:50%;background:var(--black);border:2px solid #fff;display:block}
.slider-dots i.on{background:var(--red)}
.join{left:739px;top:8px;width:318px;height:325px;border-radius:12px;background:var(--black);color:var(--white);overflow:hidden}
.join-head{left:6px;top:6px;width:303px;height:62px;border-radius:12px;background:linear-gradient(180deg,#fffbd0,#ffe03a);
  display:flex;align-items:center;padding-left:12px;gap:6px}
.join-head .avatar{width:44px;height:50px;border-radius:50%;background:linear-gradient(#f7a030,#d9731a)}
.join-head p{font-weight:700;font-size:21px;line-height:26px;color:var(--black);text-align:center;flex:1}
.join-head em{font-style:normal;color:var(--red)}
.perks{left:16px;top:82px;list-style:none}
.perks li{color:var(--yellow-text);font-weight:700;font-size:15px;margin-bottom:10px}
.perks li::before{content:"»";color:#ddd;margin-right:8px;font-size:12px}
.join-arc{left:-40px;top:185px;width:400px;height:200px;border-radius:50%;border-top:2px solid #b08a14;background:radial-gradient(ellipse at 50% 0,rgba(120,90,10,.6),transparent 60%)}
.join-form label{position:absolute;font-size:13px;color:#eee}
.join-form .field{position:absolute;left:83px;width:170px;height:22px;background:linear-gradient(#ddd,#fff)}
.btn{display:inline-flex;align-items:center;justify-content:center;border-radius:8px;color:var(--white);font-weight:700;font-size:12px;
  background:linear-gradient(180deg,#fbb440,#e8521f);border:1px solid #fff3c0;box-shadow:0 1px 2px rgba(0,0,0,.4)}

/* offer cards */
.card{top:600px;width:350px;height:247px;border-radius:10px;overflow:hidden;border:2px solid #fff3c0;box-shadow:0 2px 5px rgba(0,0,0,.35)}
.card-photo{position:absolute;inset:0}
.card-label{position:absolute;left:7px;bottom:8px;font-size:19px;color:var(--black);text-shadow:0 0 3px #fff,0 0 3px #fff,0 0 2px #fff}
.card .btn{position:absolute;height:28px;bottom:8px}
.pt .card-photo{background:linear-gradient(180deg,#f3f3f0 0%,#d8dde0 45%,#93a862 75%,#6f8b3c 100%)}
.pt .bubble{left:-30px;top:-70px;width:260px;height:190px;border-radius:50%;background:var(--black);color:var(--white);padding:88px 0 0 44px;font-size:18px;line-height:26px}
.gf .card-photo{background:linear-gradient(180deg,#f6d21a 0%,#eec019 40%,#2b2b20 70%,#111 100%)}
.gf .photo-a{left:14px;top:52px;width:165px;height:185px;transform:rotate(-5deg);border:4px solid #fff;background:linear-gradient(#b9c7d6,#79894d)}
.gf .photo-b{left:180px;top:18px;width:140px;height:160px;transform:rotate(7deg);border:4px solid #fff;background:linear-gradient(#8fc4d8,#d99a7a)}
.gf .headline{left:8px;top:8px;font-size:18px;line-height:26px;color:var(--black)}
.bc .card-photo{background:linear-gradient(120deg,#c3a27a 0%,#a7b489 40%,#d7d5cc 70%,#bcb6a8 100%)}
.bc .ribbon{left:118px;top:112px;width:270px;height:54px;background:var(--black);transform:rotate(-33deg);color:var(--yellow-text);font-size:14px;display:flex;align-items:center;justify-content:center;white-space:nowrap;padding-right:20px}
.red{color:var(--red)}
.amber{color:var(--gold)}

/* welcome */
.welcome{left:28px;top:862px;width:812px}
.welcome h1{font-size:26px;font-weight:400;color:var(--black);text-shadow:0 0 3px #fff,0 0 3px #fff;margin-bottom:6px}
.welcome h1 span{color:var(--red);font-weight:700}
.welcome p{font-size:12.3px;line-height:15.7px;margin:0 0 16px 4px}
.welcome h4{font-size:15px;font-weight:700;margin:-4px 0 6px 4px}
.video{left:849px;top:873px;width:242px;height:220px;border:5px solid var(--orange);box-shadow:0 2px 5px rgba(0,0,0,.3);
  background:linear-gradient(180deg,#eef0f2 0%,#c8d0d6 60%,#a6b0b6 100%);display:flex;align-items:center;justify-content:center}
.play{width:82px;height:82px;border-radius:50%;background:rgba(90,90,90,.7);border:5px solid #ddd;display:flex;align-items:center;justify-content:center}

/* footer */
.site-footer{left:26px;top:1138px;width:1062px;height:42px;border-radius:12px;border:2px solid #fff3c0;
  background:linear-gradient(180deg,#fbc24a,#ef8a1c 55%,#e8521f);display:flex;align-items:center;justify-content:center;font-size:11.5px;color:var(--black);box-shadow:0 2px 5px rgba(0,0,0,.35)}
</style>
</head>
<body>

<header class="site-header abs">
  <div class="brand abs"><span class="brand-dot"></span><span class="brand-name">VANTOR</span></div>
  <div class="call abs">
    <span class="call-icon"><svg width="30" height="30" viewBox="0 0 24 24"><path fill="#fff" d="M6.6 10.8a15.1 15.1 0 0 0 6.6 6.6l2.2-2.2a1 1 0 0 1 1-.25 11.4 11.4 0 0 0 3.6.57 1 1 0 0 1 1 1V20a1 1 0 0 1-1 1A17 17 0 0 1 3 4a1 1 0 0 1 1-1h3.5a1 1 0 0 1 1 1c0 1.25.2 2.45.57 3.57a1 1 0 0 1-.25 1z"/></svg></span>
    <span class="call-text"><b>Call</b> 1300 555 019</span>
  </div>
  <nav class="quick-links abs">
    <a class="quick-link" href="#"><svg viewBox="0 0 50 50"><circle cx="20" cy="20" r="17" fill="#eef3f8" stroke="#4f7fb0" stroke-width="3"/><path d="M20 9v11l7 4" stroke="#333" stroke-width="2.5" fill="none"/><rect x="24" y="26" width="22" height="20" fill="#fff" stroke="#5a9c3a" stroke-width="2"/><rect x="24" y="26" width="22" height="5" fill="#5a9c3a"/></svg>Time Table</a>
    <a class="quick-link" href="#"><svg viewBox="0 0 50 50"><path d="M4 14l13-5 16 5 13-5v30l-13 5-16-5-13 5z" fill="#8cc76a" stroke="#3c7a3a" stroke-width="1.5"/><path d="M25 6a7 7 0 0 1 7 7c0 6-7 13-7 13s-7-7-7-13a7 7 0 0 1 7-7z" fill="#e3241b"/><circle cx="25" cy="13" r="2.5" fill="#fff"/></svg>Club Locations</a>
    <a class="quick-link" href="#"><svg viewBox="0 0 50 50"><circle cx="18" cy="12" r="8" fill="none" stroke="#ccc" stroke-width="4"/><path d="M18 20v24l4-3v-4l-3-2 3-2" stroke="#bbb" stroke-width="4" fill="none"/><circle cx="30" cy="16" r="7" fill="none" stroke="#999" stroke-width="4"/><path d="M30 23v22" stroke="#999" stroke-width="4"/></svg>Login</a>
  </nav>
  <nav class="main-nav abs">
    <a class="current" href="#">Home</a>
    <a href="#">About Us</a>
    <a href="#">Fitness</a>
    <a href="#">Events &amp; Adventures</a>
    <a href="#">Contact Us</a>
  </nav>
</header>

<section class="feature abs">
  <div class="slider abs" role="img" aria-label="Photo of smiling cyclists and a woman stretching on grass in a sunny park">
    <div class="slide-caption abs">
      <h2>Title Goes Here</h2>
      <h3>Subtitle Comes here</h3>
      <p>Lorem ipsum dolor sit amet consecutor. Lorem ipsum dolor sit amet consecutor. Lorem ipsum dolor sit amet consecutor. Lorem ipsum dolor sit amet consecutor.</p>
      <p class="more">Lorem ipsum dolor</p>
    </div>
    <div class="slider-dots abs"><i class="on"></i><i></i><i></i><i></i><i></i></div>
  </div>
  <aside class="join abs">
    <div class="join-arc abs"></div>
    <div class="join-head abs">
      <span class="avatar" role="img" aria-label="Member icon"></span>
      <p><em>FREE</em> Membership,<br>Join Us: <em>(valued $65)</em></p>
    </div>
    <ul class="perks abs">
      <li>Monthly E-News Hints, Tips &amp; Advice</li>
      <li>VIP Invites Events &amp; Adventures</li>
      <li>Special Member Only Offers</li>
      <li>Discount Card to 20+Providers</li>
    </ul>
    <form class="join-form">
      <label style="left:36px;top:214px">Name:</label><span class="field" style="top:211px"></span>
      <label style="left:34px;top:243px">Email:</label><span class="field" style="top:240px"></span>
      <span class="btn abs" style="left:154px;top:271px;width:97px;height:29px">Join Us</span>
    </form>
  </aside>
</section>

<article class="card pt abs" style="left:26px">
  <div class="card-photo" role="img" aria-label="Photo of a woman in a yoga pose on a grassy hilltop"></div>
  <div class="bubble abs"><span class="red">Free</span> initial Consult &amp;<br>1-on-1 Session<br><span class="amber">(valued $80.00)</span></div>
  <span class="card-label">Personal Training</span>
  <span class="btn" style="right:7px;width:96px">More</span>
</article>

<article class="card gf abs" style="left:385px">
  <div class="card-photo"></div>
  <div class="photo-a abs" role="img" aria-label="Photo of a group running outdoors"></div>
  <div class="photo-b abs" role="img" aria-label="Photo of a smiling group fitness class"></div>
  <div class="headline abs">Intro Pass <span class="red">$25</span><br><span class="red">7 Days</span> Unlimited<br>Classes</div>
  <span class="card-label">Group Fitness</span>
  <span class="btn" style="right:7px;width:96px">More</span>
</article>

<article class="card bc abs" style="left:744px">
  <div class="card-photo" role="img" aria-label="Photo of a boot camp group doing push-ups outdoors"></div>
  <div class="ribbon abs">Starts soon #'s Limited</div>
  <span class="card-label">Boot Camp</span>
  <span class="btn" style="left:141px;width:96px">More Info</span>
  <span class="btn" style="right:7px;width:96px">Enlist</span>
</article>

<section class="welcome abs">
  <h1>Welcome to <span>VANTOR</span></h1>
  <p>Lorem ipsum dolor sit amet consecutor. Lorem ipsum dolor sit amet consecutor. Lorem ipsum dolor sit amet consecutor. Lorem ipsum dolor sit amet consecutor. Lorem ipsum dolor sit amet consecutor. Lorem ipsum dolor sit amet consecutor. Lorem ipsum dolor sit amet consecutor. Lorem ipsum dolor sit amet consecutor. Lorem ipsum dolor sit amet consecutor.. Lorem ipsum dolor sit amet consecutor. Lorem ipsum dolor sit amet consecutor. Lorem ipsum dolor sit amet consecutor. Lorem ipsum dolor sit amet consecutor.</p>
  <h4>Lorem ipsum dolor</h4>
  <p>Lorem ipsum dolor sit amet consecutor. Lorem ipsum dolor sit amet consecutor. Lorem ipsum dolor sit amet consecutor. Lorem ipsum dolor sit amet consecutor. Lorem ipsum dolor sit amet consecutor. Lorem ipsum dolor sit amet consecutor. Lorem ipsum dolor sit amet consecutor. Lorem ipsum dolor sit amet consecutor. Lorem ipsum dolor sit amet consecutor.. Lorem ipsum dolor sit amet consecutor. Lorem ipsum dolor sit amet consecutor. Lorem ipsum dolor sit amet consecutor. Lorem ipsum dolor sit amet consecutor.</p>
  <p>Lorem ipsum dolor sit amet consecutor. Lorem ipsum dolor sit amet consecutor. Lorem ipsum dolor sit amet consecutor. Lorem ipsum dolor sit amet consecutor. Lorem ipsum dolor sit amet consecutor. Lorem ipsum dolor sit amet consecutor. Lorem ipsum dolor sit amet consecutor. Lorem ipsum dolor sit amet consecutor. Lorem ipsum dolor sit amet consecutor.</p>
</section>

<div class="video abs" role="img" aria-label="Video still of a woman doing push-ups, with a play button">
  <span class="play"><svg width="38" height="40" viewBox="0 0 38 40"><path d="M6 2l30 18-30 18z" fill="#eee"/></svg></span>
</div>

<footer class="site-footer abs">Vantor ©&nbsp; 2011 All Rights Reserved &nbsp;|&nbsp; Privacy Policy</footer>

</body>
</html>
```